Civic Shieldpoint Company

We have design at www.vexaloft.com and want
New site design
Carallax
Images added
Were looking for your eyes. Just placement and look and feel. No hard coding. Design only.

Industry/Entity Type

It Company

```html
<!DOCTYPE html>
<html lang="en">
<head>
<meta charset="utf-8">
<title>Vexaloft – Fraud Protection</title>
<link href="https://fonts.googleapis.com/css2?family=Carlito:wght@400;700&family=Open+Sans:wght@400;600;700&display=swap" rel="stylesheet">
<style>
  :root {
    --page-bg: #f1f1f1;
    --panel-bg: #ffffff;
    --login-bg: #f8f8f8;
    --bar-top: #6fa3d6;
    --bar-mid: #3b78b8;
    --bar-bottom: #23609f;
    --tab-light-top: #a9c6e6;
    --tab-light-bottom: #7fa7d3;
    --headline: #2f6fae;
    --link: #2a66a3;
    --text: #444444;
    --field-top: #c9c9c9;
    --field-bottom: #8c8c8c;
    --field-border: #9a9a9a;
    --map-light: #e4f2d2;
    --map-dark: #b9dc93;
  }
  * { box-sizing: border-box; margin: 0; padding: 0; }
  html, body { width: 1200px; height: 675px; overflow: hidden; background: var(--page-bg); }
  body { font-family: "Open Sans", Arial, sans-serif; color: var(--text); position: relative; }

  .bar {
    background: linear-gradient(to bottom, var(--bar-top) 0%, var(--bar-mid) 45%, var(--bar-bottom) 100%);
    color: #fff;
  }

  /* top navigation */
  .site-nav { position: absolute; left: 0; top: 0; width: 1200px; height: 40px; display: flex; }
  .brand {
    width: 113px; height: 40px; display: flex; align-items: center; justify-content: center;
    font-size: 18px; font-weight: 600; color: #fff; letter-spacing: .5px;
  }
  .nav-tabs {
    display: flex; width: 470px; height: 40px;
    background: linear-gradient(to bottom, var(--tab-light-top), var(--tab-light-bottom));
  }
  .nav-tabs a {
    flex: 1; display: flex; align-items: center; justify-content: center;
    color: #fff; text-decoration: none; font-weight: 700; font-size: 15px;
    text-shadow: 0 1px 1px rgba(0,0,0,.25);
  }
  .nav-tabs a.home { background: linear-gradient(to bottom, #8fb4dc, #5f8fc4); flex: 0 0 69px; }
  .nav-spacer { flex: 1; }
  .nav-login {
    width: 69px; display: flex; align-items: center; justify-content: center;
    font-weight: 700; font-size: 15px; color: #fff;
    background: linear-gradient(to bottom, var(--tab-light-top), var(--tab-light-bottom));
  }

  /* news ticker */
  .news-ticker {
    position: absolute; left: 24px; top: 71px; width: 1153px; height: 24px;
    display: flex; align-items: center; font-size: 11px; overflow: hidden; white-space: nowrap;
  }
  .news-label {
    height: 100%; display: flex; align-items: center; padding: 0 10px 0 9px;
    font-weight: 700; background: #2a6aa9; margin-right: 8px;
  }

  /* hero */
  .hero {
    position: absolute; left: 24px; top: 116px; width: 883px; height: 309px;
    background: var(--panel-bg);
  }
  .hero-title {
    position: absolute; left: 11px; top: 22px; font-family: "Carlito", Calibri, sans-serif;
    font-size: 64px; line-height: 80px; font-weight: 400; color: var(--headline);
    text-shadow: 2px 3px 3px rgba(0,0,0,.25);
  }
  .hero-link {
    position: absolute; left: 10px; top: 178px; font-family: "Carlito", Calibri, sans-serif;
    font-size: 15px; color: var(--link);
  }
  .hero-map {
    position: absolute; left: 497px; top: 104px; width: 384px; height: 200px;
    background: linear-gradient(135deg, var(--map-light), var(--map-dark));
  }

  /* login panel */
  .login-panel {
    position: absolute; left: 921px; top: 116px; width: 256px; height: 309px;
    background: var(--login-bg);
  }
  .panel-header {
    height: 32px; display: flex; align-items: center; padding-left: 9px;
    font-size: 11px; font-weight: 700;
  }
  .login-form { margin-top: 43px; }
  .field-label { text-align: center; font-size: 15px; font-weight: 600; color: #4a4a4a; }
  .field-label.password { margin-top: 16px; }
  .field {
    margin: 5px auto 0; width: 235px; height: 41px; border: 3px solid var(--field-border);
    background: linear-gradient(to bottom, var(--field-top), var(--field-bottom));
    display: flex; align-items: center; justify-content: center;
    color: #fff; font-weight: 700; font-size: 12px;
  }
  .forgot { display: block; text-align: center; margin-top: 16px; font-size: 8px; color: var(--link); }
  .sign-in {
    position: absolute; right: 8px; bottom: 8px; width: 86px; height: 23px;
    display: flex; align-items: center; justify-content: flex-end; gap: 6px; padding-right: 4px;
    font-size: 11px; font-weight: 700;
  }

  /* content panel */
  .content-panel {
    position: absolute; left: 25px; top: 445px; width: 1154px; height: 227px;
    background: var(--panel-bg);
  }
  .content-panel .panel-header { height: 26px; }
  .content-title {
    margin-top: 56px; text-align: center; font-size: 12.5px; font-weight: 700; color: #444;
  }
  .content-body {
    margin: 19px 10px 0; text-align: center; font-size: 12.4px; line-height: 18.5px;
    color: #444; white-space: nowrap;
  }
</style>
</head>
<body>
  <header class="site-nav bar">
    <div class="brand">Vexaloft</div>
    <nav class="nav-tabs">
      <a class="home" href="#">Home</a>
      <a href="#">Tab 1</a>
      <a href="#">Tab 2</a>
      <a href="#">Tab 3</a>
      <a href="#">Tab 4</a>
    </nav>
    <div class="nav-spacer"></div>
    <div class="nav-login">Login</div>
  </header>

  <div class="news-ticker bar">
    <span class="news-label">News</span>
    <span>in the latest contactless card scandal. Several banks in Cyprus shut down after going bankrupt. A new scam has been created with Payvora prepaid cards allowing people to transfer money without a pin or address. A spo</span>
  </div>

  <section class="hero">
    <h1 class="hero-title">Vexaloft can protect you<br>against fraud.</h1>
    <a class="hero-link" href="#">Click here to find out more &gt;&gt;</a>
    <div class="hero-map" role="img" aria-label="Illustration: green world map with location pins marking a user and a flagged card transaction"></div>
  </section>

  <aside class="login-panel">
    <div class="panel-header bar">Login</div>
    <div class="login-form">
      <div class="field-label">Email Address</div>
      <div class="field">Email@domain.com</div>
      <div class="field-label password">Password</div>
      <div class="field">**************</div>
      <a class="forgot" href="#">Forgot your password?</a>
    </div>
    <div class="sign-in bar">
      Sign In
      <svg width="16" height="20" viewBox="0 0 16 20" aria-hidden="true">
        <path d="M4 9V6a4 4 0 0 1 8 0v3" fill="none" stroke="#bbb" stroke-width="2"/>
        <rect x="1" y="9" width="14" height="11" rx="1" fill="#c9a94a"/>
      </svg>
    </div>
  </aside>

  <section class="content-panel">
    <div class="panel-header bar">Your Text Goes Here?</div>
    <h2 class="content-title">sprechgesang alleviated rototiller shiite yssel mizar unharmonized</h2>
    <p class="content-body">uncorrelated roundworm unfathomed remittor interfilling deforce. Dodecastylar pointlessness overconcern pontianus antimodern proportioned redraft unhumoured cubby nonacid<br>malignantly streamless hadley boyne. Spathose fideicommissa motherland anopheles fry wrester forewarn prelabeled scottie stannary polyandrist offender forme nondeterministic.<br>Currish undercomment lickspit drumfish untidied unadvantageous gaddi preindisposing bibliotics unabetting wasteland loz spiritoso antienergistic. Gobstopper malthusian insecure</p>
  </section>
</body>
</html>
```